Tidal Spoon is a modern and professional services business in the field of hospitality.

Need business card for a professional chef and consultant. Attention to detail and to stand out is our goal. I want a professional and stand out card which is not generic.
Would like a modern card with black gold or blue I’m not very sure on colours yet , open to ideas from those in the know. This is my second project and have been really happy with the process so far.
With 15 years in the hospitality industry I am launching into consulting and starting my own business. I’d like a few types of designs to look at which style I want. Open to suggestions. Thanks in advance for the work. I want something that will become part of my brand as it is launched. There is a chance for possible future work to the right person.

Target Market(s)

Restauranters and Registered training organisations.

Industry/Entity Type

Professional Service

Font styles to use
Serif

Colors

Designer to choose colors to be used in the design.

Requirements
Must have
• A stand out design, blue / black
Nice to have
• Can u get embossed cards?
Should not have
• Na

```html
<!DOCTYPE html>
<html lang="en">
<head>
<meta charset="utf-8">
<title>Tidal Spoon – Business Card</title>
<link rel="stylesheet" href="https://fonts.googleapis.com/css2?family=Playfair+Display:wght@500;600&family=Lora:wght@400;600&display=swap">
<style>
  :root {
    --backdrop: #2a2b2e;
    --card: #111318;
    --card-edge: #1b1e25;
    --accent-blue: #3d8fdc;
    --silver: #b4b8bf;
    --ink-light: #eef1f5;
  }
  * { margin: 0; padding: 0; box-sizing: border-box; }
  html, body {
    width: 1200px; height: 900px; overflow: hidden;
    background: var(--backdrop);
  }
  .stage {
    position: relative; width: 1200px; height: 900px;
    display: flex; align-items: center; justify-content: center; gap: 40px;
  }
  .card {
    position: relative; width: 500px; height: 286px;
    background: linear-gradient(160deg, var(--card-edge), var(--card));
    border-radius: 18px;
    box-shadow: 0 18px 40px rgba(0,0,0,.45);
  }
  /* back side */
  .card-back .brand-mark {
    position: absolute; left: 30px; top: 0; bottom: 0; width: 230px;
    display: flex; align-items: center; justify-content: center;
    font-family: "Playfair Display", serif; font-weight: 600;
    font-size: 32px; color: var(--accent-blue); white-space: nowrap;
  }
  .contact {
    position: absolute; left: 275px; top: 56px; right: 16px;
    font-family: "Lora", serif; color: var(--ink-light);
    font-size: 13.5px; line-height: 1.35;
  }
  .contact .person-name {
    font-family: "Playfair Display", serif;
    font-weight: 600; font-size: 20px; color: var(--accent-blue); line-height: 1.15;
  }
  .contact .person-role { margin-bottom: 14px; }
  .contact .address { margin-bottom: 14px; }
  .contact ul { list-style: none; }
  .contact li { display: flex; align-items: center; gap: 10px; white-space: nowrap; }
  .contact svg { width: 12px; height: 12px; fill: var(--accent-blue); flex: none; }
  .contact .icon-web { fill: none; stroke: var(--accent-blue); stroke-width: 2; }
  /* front side */
  .card-front {
    display: flex; align-items: center; justify-content: center; gap: 16px;
  }
  .card-front .dot {
    width: 20px; height: 20px; border-radius: 50%; background: var(--accent-blue);
  }
  .card-front .brand-name {
    font-family: "Playfair Display", serif; font-weight: 500;
    font-size: 50px; letter-spacing: 2px; color: var(--silver); white-space: nowrap;
  }
</style>
</head>
<body>
<main class="stage">
  <section class="card card-back">
    <div class="brand-mark">Tidal Spoon</div>
    <div class="contact">
      <p class="person-name">Marcus Reed</p>
      <p class="person-role">Managing Director</p>
      <p class="address">48 Harbour Lane<br>Port Ellis, 204519.</p>
      <ul>
        <li><svg viewBox="0 0 24 24"><path d="M6.6 10.8a15 15 0 0 0 6.6 6.6l2.2-2.2a1 1 0 0 1 1-.25 11.4 11.4 0 0 0 3.6.57 1 1 0 0 1 1 1V20a1 1 0 0 1-1 1A17 17 0 0 1 3 4a1 1 0 0 1 1-1h3.5a1 1 0 0 1 1 1c0 1.25.2 2.45.57 3.57a1 1 0 0 1-.25 1z"/></svg>044-987 210 365</li>
        <li><svg viewBox="0 0 24 24"><path d="M2 5h20v14H2zm2 2v.5l8 5 8-5V7l-8 5z"/></svg>hello@tidalspoon.com</li>
        <li><svg class="icon-web" viewBox="0 0 24 24"><circle cx="12" cy="12" r="9"/><path d="M3 12h18M12 3c3 3 3 15 0 18M12 3c-3 3-3 15 0 18"/></svg>www.tidalspoon.com</li>
      </ul>
    </div>
  </section>
  <section class="card card-front">
    <span class="dot"></span>
    <span class="brand-name">TIDAL SPOON</span>
  </section>
</main>
</body>
</html>
```